Banner for construction site to identify developer

we need a 4 foot by 8 foot banner to hang on the fence of a residential townhome development in Phoenix, Arizona that identifies Tolvane Holdings as the company behind the development/project. Also needs to include the logo, phone number, and web address. Would like to stick with the blue colors provided in the attached logo. The blues should stay the same but the letters in the logo can change to another color if necessary. Feel free to use "Tolvane Holdings" in place of "Tolvane Holdings Group". Looking for use of colors/design to take up space so banner is not just text with a logo.

Target Market(s)

drive by traffic looking at the site

Industry/Entity Type

Real Estate

Colors
0054AA
0677BA
7BADD7
CADEEF
E8F1F8

Requirements
Must have
• company name, phone number and web address

```html
<!DOCTYPE html>
<html lang="en">
<head>
<meta charset="utf-8">
<title>Tolvane Holdings – Site Banner</title>
<link rel="stylesheet" href="https://fonts.googleapis.com/css2?family=Open+Sans:wght@700&family=Oswald:wght@500&display=swap">
<style>
  :root {
    --page-bg: #e6ecf3;
    --white: #ffffff;
    --charcoal: #333336;
    --sky-blue: #1ea6e0;
    --deep-blue: #1f72ad;
    --name-ink: #2f3033;
  }
  * { box-sizing: border-box; margin: 0; padding: 0; }
  html, body {
    width: 1200px;
    height: 900px;
    overflow: hidden;
    background: var(--page-bg);
  }
  .canvas {
    position: relative;
    width: 1200px;
    height: 900px;
    display: flex;
    align-items: center;
    justify-content: center;
  }
  .banner {
    position: relative;
    width: 400px;
    height: 860px;
    overflow: hidden;
    background: var(--white);
    box-shadow: 0 4px 18px rgba(20, 40, 70, 0.18);
  }
  .banner-shapes {
    position: absolute;
    inset: 0;
    width: 100%;
    height: 100%;
  }
  .brand {
    position: absolute;
    left: 0;
    right: 0;
    top: 200px;
    display: flex;
    flex-direction: column;
    align-items: center;
    gap: 22px;
  }
  .brand-square {
    width: 34px;
    height: 34px;
    background: var(--sky-blue);
  }
  .brand-name {
    font-family: "Open Sans", Arial, sans-serif;
    font-weight: 700;
    font-size: 40px;
    line-height: 1;
    letter-spacing: -0.5px;
    color: var(--name-ink);
    white-space: nowrap;
  }
  .contact {
    position: absolute;
    left: 52px;
    top: 572px;
    display: flex;
    flex-direction: column;
    gap: 22px;
  }
  .contact-row {
    display: flex;
    align-items: center;
    gap: 12px;
    color: var(--white);
    white-space: nowrap;
  }
  .contact-icon {
    width: 28px;
    height: 28px;
    flex: none;
  }
  .contact-phone {
    font-family: "Oswald", "Arial Narrow", sans-serif;
    font-weight: 500;
    font-size: 31px;
    line-height: 1;
  }
  .contact-web {
    font-family: "Open Sans", Arial, sans-serif;
    font-weight: 700;
    font-size: 21px;
    line-height: 1;
  }
</style>
</head>
<body>
<main class="canvas">
  <section class="banner" aria-label="Tolvane Holdings site banner">
    <svg class="banner-shapes" viewBox="0 0 400 860" preserveAspectRatio="none" aria-hidden="true">
      <path d="M0 448 C120 402 280 372 400 382 L400 860 L0 860 Z" fill="var(--charcoal)"/>
      <path d="M0 472 C120 432 280 410 400 420 L400 860 L0 860 Z" fill="var(--sky-blue)"/>
      <path d="M0 500 C140 470 280 455 400 462 L400 860 L0 860 Z" fill="var(--deep-blue)"/>
      <circle cx="332" cy="884" r="164" fill="var(--sky-blue)"/>
    </svg>

    <div class="brand">
      <span class="brand-square" aria-hidden="true"></span>
      <h1 class="brand-name">Tolvane Holdings</h1>
    </div>

    <div class="contact">
      <p class="contact-row">
        <svg class="contact-icon" viewBox="0 0 28 28" aria-hidden="true">
          <circle cx="14" cy="14" r="13" fill="var(--white)"/>
          <path d="M10.2 7.5 c0.6-0.4 1.3-0.2 1.6 0.4 l1.3 2.4 c0.3 0.6 0.1 1.2-0.4 1.6 l-1 0.7 c0.7 1.6 1.9 2.9 3.5 3.6 l0.7-1 c0.4-0.5 1-0.7 1.6-0.4 l2.4 1.3 c0.6 0.3 0.8 1 0.4 1.6 l-0.9 1.4 c-0.5 0.7-1.4 1.1-2.3 0.9 C12.7 19.4 8.6 15.3 7.5 10.9 c-0.2-0.9 0.2-1.8 0.9-2.3 Z" fill="var(--sky-blue)"/>
        </svg>
        <span class="contact-phone">480-555-0176</span>
      </p>
      <p class="contact-row">
        <svg class="contact-icon" viewBox="0 0 28 28" aria-hidden="true">
          <circle cx="14" cy="14" r="13" fill="var(--white)"/>
          <g fill="none" stroke="var(--sky-blue)" stroke-width="1.6">
            <circle cx="14" cy="14" r="7.5"/>
            <ellipse cx="14" cy="14" rx="3.2" ry="7.5"/>
            <line x1="6.5" y1="14" x2="21.5" y2="14"/>
          </g>
        </svg>
        <span class="contact-web">www.TolvaneHoldings.com</span>
      </p>
    </div>
  </section>
</main>
</body>
</html>
```